Corvell Tarn manufacturing Project

We are looking at getting a brand new design for a new company that deals in selling stainless tubing and other stainless still products such as handrails, Spigots, Balustrade Fittings
Glass, Glass fittings and Aluminium Channels

We require a very clean website that deals with the following colours:

Blue to light blues
Blacks
Greys to light Greys
Whites

We are open for other ideas BUT we *DO NOT* want any pinks, greens or bright colours except for backgrounds colours we have chosen above. (It can be solid, gradient or a subtle pattern)

YOU MUST KEEP THE LOGO AS IS. PLEASE DO NOT ALTER THE LOGO IN *ANY WAY* and the logo MUST be the same colours and fonts.

Logo is attached.

The site must contain these aspects:
jQuery Slider (Image slide show)
Top drop down Menus
Be no more than 900px wide
Text is to be to the k9R standards. (no special fonts)

We will chop up the design into html format. You just need to provide the PSD file.

The clients opposition is:
www.polbrenwick.com

It Company

• Alter the logo in anyway

```html
<!DOCTYPE html>
<html lang="en">
<head>
<meta charset="utf-8">
<title>Corvell Tarn Manufacturing Co. Ltd</title>
<link rel="stylesheet" href="https://fonts.googleapis.com/css2?family=Arimo:wght@400;700&family=Source+Sans+3:wght@400;600&display=swap">
<style>
:root{
  --blue-dark:#2a4f80;
  --blue-mid:#4a72ab;
  --blue-light:#7fa6dc;
  --nav-top:#6f95c9;
  --nav-bottom:#3b5e93;
  --grey-bar:#e4e4e4;
  --grey-line:#b9b9b9;
  --text:#1b1b1b;
  --footer-bottom:#474747;
  --white:#ffffff;
}
*{margin:0;padding:0;box-sizing:border-box}
html,body{width:880px;height:1200px;overflow:hidden;background:var(--white)}
body{position:relative;font-family:"Arimo",Arial,sans-serif;color:var(--text)}
.abs{position:absolute}

/* top strip */
.topbar{left:0;top:0;width:880px;height:35px;background:linear-gradient(#f4f4f4,#dcdcdc);border-bottom:1px solid #cfcfcf}
.topbar-item{top:11px;font-size:11px;color:#333;display:flex;align-items:center;gap:7px}
.topbar-item svg{flex:none}
.social{top:8px;width:20px;height:20px;border-radius:50%;background:radial-gradient(circle at 40% 35%,#6f93c8,#2f5389)}

/* header */
.header{left:0;top:35px;width:880px;height:154px;background:linear-gradient(#ffffff,#ececec 75%,#e2e2e2)}
.brand-mark{left:78px;top:48px;width:84px;height:84px;border-radius:50%;background:#2d4a78}
.brand-name{left:12px;top:137px;font-family:"Arimo",Arial,sans-serif;font-weight:400;color:#111;font-size:25px;letter-spacing:-.3px}
.brand-sub{left:32px;top:165px;font-family:"Arimo",Arial,sans-serif;font-weight:400;color:#111;font-size:11.5px;letter-spacing:1.6px}
.header-visual{left:288px;top:40px;width:314px;height:149px;background:linear-gradient(90deg,#d9d9d9,#f7f7f7 30%,#bdbdbd 55%,#f2f2f2 80%,#cfcfcf);border-radius:4px}
.search{left:679px;top:155px;width:200px;height:23px;border:1px solid #bdbdbd;background:#fff;font-size:10px;color:#333;padding:5px 8px;letter-spacing:.3px}
.search svg{position:absolute;right:6px;top:4px}

/* navigation */
.nav{left:0;top:189px;width:880px;height:25px;background:linear-gradient(var(--nav-top),var(--nav-bottom));display:flex}
.nav-item{height:25px;line-height:25px;color:var(--white);font-size:11px;font-weight:700;text-align:center;border-right:1px solid #8aa9d6;letter-spacing:.2px}
.nav-item.is-active{background:linear-gradient(#3e6299,#24436f);font-size:12px}

/* slider */
.slider{left:0;top:214px;width:880px;height:322px;background:linear-gradient(100deg,#c9c6c0,#e9e7e3 35%,#f4f3f0 60%,#d4d1cc);}
.slide-title{left:14px;top:238px;font-size:27px;color:#5a5a5a;letter-spacing:-.5px}
.slide-copy{left:14px;top:265px;font-size:21px;line-height:23px;color:#5a5a5a;letter-spacing:-.3px}
.slide-arrow{top:491px;width:26px;height:25px;background:linear-gradient(#6f95c9,#3b5e93);display:flex;align-items:center;justify-content:center}
.slider-shadow{left:40px;top:536px;width:800px;height:26px;background:radial-gradient(ellipse at 50% 0%,rgba(0,0,0,.16),rgba(0,0,0,0) 70%)}

/* content columns */
.col-title{top:586px;font-family:"Arimo",Arial,sans-serif;font-weight:700;font-size:17px;color:var(--blue-dark);letter-spacing:.2px}
.col-text{top:616px;width:250px;font-family:"Source Sans 3",Arial,sans-serif;font-size:11.3px;line-height:14.6px;color:var(--text)}
.col-text p{margin-bottom:14.6px}
.divider{top:588px;width:1px;height:338px;background:var(--grey-line)}
.btn-more{top:894px;width:79px;height:26px;background:linear-gradient(#6f95c9,#35588d);color:var(--white);font-size:10.5px;font-weight:700;line-height:26px;text-align:center;box-shadow:0 1px 2px rgba(0,0,0,.3)}

.event-date{left:598px;font-size:11.5px;color:#444}
.event-photo{left:598px;width:110px;height:131px;border:1px solid #c7c7c7;padding:4px;background:#fff}
.event-photo div{width:100%;height:100%}
.event-text{left:711px;width:170px;font-size:11px;line-height:13.7px;color:var(--text)}
.btn-small{left:711px;width:77px;height:16px;background:linear-gradient(#6f95c9,#35588d);color:var(--white);font-size:9.5px;line-height:16px;text-align:center}
.event-rule{left:598px;top:772px;width:272px;border-top:1px dashed #bcbcbc}

/* footer */
.footer{left:0;top:964px;width:880px;height:208px;background:linear-gradient(#79a2da,#5a82bd 50%,#3c5f96)}
.footer-title{top:989px;font-size:17.5px;color:var(--white)}
.footer-divider{top:990px;height:160px;border-left:1px dotted #d5e2f5}
.footer-menu{left:43px;top:1019px;list-style:none;font-size:9.6px;color:var(--white);line-height:19.6px}
.avatar{left:178px;width:53px;height:53px;border-radius:50%;background:radial-gradient(circle at 45% 40%,#9fb1cc,#2d4a78 60%,#1c1c1c);border:2px solid #d0d0d0}
.tweet{left:249px;font-size:11.5px;line-height:14px;color:var(--white)}
.tweet-time{left:341px;top:1070px;font-size:8.5px;color:var(--white)}
.contact-line{left:429px;font-size:11.5px;line-height:13px;color:var(--white);display:flex;gap:8px;align-items:flex-start}
.email-field{left:642px;top:1024px;width:191px;height:31px;background:#f1f1f1;border:1px solid #c5c5c5;font-size:12px;color:#222;padding:8px 9px}
.subscribe{left:642px;top:1070px;width:73px;height:26px;background:linear-gradient(#6f95c9,#35588d);color:var(--white);font-size:12px;line-height:26px;text-align:center;box-shadow:0 1px 2px rgba(0,0,0,.3)}
.copyright{left:0;top:1172px;width:880px;height:28px;background:var(--footer-bottom);color:var(--white);font-size:10.5px;line-height:28px;text-align:center}
</style>
</head>
<body>

<!-- top strip -->
<div class="abs topbar"></div>
<div class="abs topbar-item" style="left:12px;top:9px">
  <svg width="12" height="18" viewBox="0 0 12 18"><circle cx="6" cy="11" r="5" fill="none" stroke="#444" stroke-width="2"/><rect x="4" y="1" width="4" height="4" fill="#444"/></svg>
  <span>your address here your address here</span>
</div>
<div class="abs topbar-item" style="left:232px">
  <svg width="18" height="15" viewBox="0 0 18 15"><path d="M3 1 L6 1 L7 5 L5 6 Q7 10 11 11 L12 9 L16 10 L16 13 Q10 15 5 10 Q1 6 3 1Z" fill="#444"/></svg>
  <span>123 456 7890 123</span>
</div>
<div class="abs topbar-item" style="left:372px">
  <svg width="16" height="12" viewBox="0 0 16 12"><rect x="0" y="0" width="16" height="12" fill="#444"/><path d="M0 0 L8 6 L16 0" fill="none" stroke="#ddd" stroke-width="1.4"/></svg>
  <span>info@youremail.com</span>
</div>
<div class="abs social" style="left:782px"></div>
<div class="abs social" style="left:805px"></div>
<div class="abs social" style="left:828px"></div>
<div class="abs social" style="left:851px"></div>

<!-- header -->
<div class="abs header"></div>
<div class="abs brand-mark"></div>
<div class="abs brand-name">Corvell Tarn</div>
<div class="abs brand-sub">Manufacturing Co. Ltd</div>
<div class="abs header-visual" role="img" aria-label="Row of polished stainless steel tubes with angled cut ends"></div>
<div class="abs search">SEARCH
  <svg width="14" height="14" viewBox="0 0 14 14"><circle cx="5.5" cy="5.5" r="4.3" fill="none" stroke="#333" stroke-width="1.5"/><path d="M8.7 8.7 L13 13" stroke="#333" stroke-width="1.8"/></svg>
</div>

<!-- navigation -->
<nav class="abs nav">
  <div class="nav-item is-active" style="width:78px">HOME</div>
  <div class="nav-item" style="width:75px">ABOUT</div>
  <div class="nav-item" style="width:96px">SERVICES</div>
  <div class="nav-item" style="width:98px">PRODUST</div>
  <div class="nav-item" style="width:101px">PARTNERS</div>
  <div class="nav-item" style="width:111px">CONTACT US</div>
</nav>

<!-- slider -->
<div class="abs slider" role="img" aria-label="Stainless steel handrail with horizontal rods beside a white floating staircase"></div>
<div class="abs slide-title">HANDRAILS</div>
<div class="abs slide-copy">Some text here Some text here<br>Some text here</div>
<div class="abs slide-arrow" style="left:801px"><svg width="10" height="12" viewBox="0 0 10 12"><path d="M7 1 L2 6 L7 11" fill="none" stroke="#fff" stroke-width="2"/></svg></div>
<div class="abs slide-arrow" style="left:830px"><svg width="10" height="12" viewBox="0 0 10 12"><path d="M3 1 L8 6 L3 11" fill="none" stroke="#fff" stroke-width="2"/></svg></div>
<div class="abs slider-shadow"></div>

<!-- who we are -->
<h2 class="abs col-title" style="left:10px">WHO WE ARE?</h2>
<div class="abs col-text" style="left:10px">
  <p>Some text here Some text here Some text here<br>Some text here Some text here Some text here.</p>
  <p>Some text here Some text here Some text here<br>Some text here Some text here Some text here<br>Some text here Some text here Some text here<br>Some text here Some text here Some text here<br>Some text here Some text here Some text here<br>Some text here Some text here Some text here<br>Some text here Some text here Some text here<br>Some text here Some text here Some text here<br>Some text here Some text here Some text here<br>Some text here Some text here Some text here<br>Some text here Some text here Some text here</p>
  <p>Some text here Some text here Some text here<br>Some text here Some text here Some text here<br>Some text here.</p>
</div>
<div class="abs btn-more" style="left:10px">Read More...</div>
<div class="abs divider" style="left:269px"></div>

<!-- what we do -->
<h2 class="abs col-title" style="left:304px">WHAT WE DO?</h2>
<div class="abs col-text" style="left:304px">
  <p>Some text here Some text here Some text here<br>Some text here Some text here Some text here.</p>
  <p>Some text here Some text here Some text here<br>Some text here Some text here Some text here<br>Some text here Some text here Some text here<br>Some text here Some text here Some text here<br>Some text here Some text here Some text here<br>Some text here Some text here Some text here<br>Some text here Some text here Some text here<br>Some text here Some text here Some text here<br>Some text here Some text here Some text here<br>Some text here Some text here Some text here<br>Some text here Some text here Some text here</p>
  <p>Some text here Some text here Some text here<br>Some text here Some text here Some text here<br>Some text here.</p>
</div>
<div class="abs btn-more" style="left:304px">Read More...</div>
<div class="abs divider" style="left:563px"></div>

<!-- upcoming events -->
<h2 class="abs col-title" style="left:598px">UPCOMING EVENTS</h2>
<div class="abs event-date" style="top:613px">June 1, 2013</div>
<div class="abs event-photo" style="top:631px"><div role="img" aria-label="Bundle of stainless steel tubes seen end on" style="background:linear-gradient(135deg,#dcdcdc,#8e8e8e 40%,#e8e8e8 70%,#6f6f6f)"></div></div>
<div class="abs event-text" style="top:630px">Some text here Some text here<br>Some text here Some text here<br>Some text here Some text here<br>Some text here Some text here<br>Some text here Some text here<br>Some text here Some text here<br>Some text here Some text here<br>Some text here Some text here</div>
<div class="abs btn-small" style="top:744px">Read More...</div>
<div class="abs event-rule"></div>
<div class="abs event-date" style="top:780px">July 1, 2013</div>
<div class="abs event-photo" style="top:799px"><div role="img" aria-label="Set of stainless steel cooking pots with glass lids" style="background:linear-gradient(135deg,#f0f0f0,#a9a9a9 45%,#e6e6e6 70%,#7d7d7d)"></div></div>
<div class="abs event-text" style="top:800px">Some text here Some text here<br>Some text here Some text here<br>Some text here Some text here<br>Some text here Some text here<br>Some text here Some text here<br>Some text here Some text here<br>Some text here Some text here<br>Some text here Some text here</div>
<div class="abs btn-small" style="top:914px">Read More...</div>

<!-- footer -->
<footer class="abs footer"></footer>
<div class="abs footer-title" style="left:43px">Menu</div>
<ul class="abs footer-menu">
  <li>HOME</li><li>ABOUT US</li><li>PICK-UP SERVICES</li><li>HOW IT WORKS</li><li>REQUEST A PICK-UP</li><li>CONTACT US</li>
</ul>
<div class="abs footer-divider" style="left:158px"></div>

<div class="abs footer-title" style="left:177px">Recet Tweets</div>
<div class="abs avatar" style="top:1017px"></div>
<div class="abs tweet" style="top:1020px">“Some text herre<br>Some text herre Some text”<br>(http://t.co/xK4mW2pLq</div>
<div class="abs tweet-time">10 min ago</div>
<div class="abs avatar" style="top:1094px"></div>
<div class="abs tweet" style="top:1097px">“Some text herre<br>Some text herre Some text”<br>(http://t.co/xK4mW2pLq</div>
<div class="abs footer-divider" style="left:409px"></div>

<div class="abs footer-title" style="left:429px">Contact us</div>
<div class="abs contact-line" style="top:1018px">
  <svg width="17" height="15" viewBox="0 0 18 15"><path d="M3 1 L6 1 L7 5 L5 6 Q7 10 11 11 L12 9 L16 10 L16 13 Q10 15 5 10 Q1 6 3 1Z" fill="#fff"/></svg>
  <span style="padding-top:2px">123 45 678900</span>
</div>
<div class="abs contact-line" style="top:1046px">
  <svg width="16" height="12" viewBox="0 0 16 12"><rect x="0" y="0" width="16" height="12" fill="#fff"/><path d="M0 0 L8 6 L16 0" fill="none" stroke="#5a82bd" stroke-width="1.4"/></svg>
  <span>info@youremail.com</span>
</div>
<div class="abs contact-line" style="top:1072px">
  <svg width="16" height="24" viewBox="0 0 16 24"><rect x="5" y="0" width="6" height="5" fill="#fff"/><circle cx="8" cy="14" r="6.5" fill="none" stroke="#fff" stroke-width="2.2"/></svg>
  <span style="padding-top:3px">Your adress here Your adress<br>here Your adress here</span>
</div>
<div class="abs footer-divider" style="left:625px"></div>

<div class="abs footer-title" style="left:642px">Sign up for our Newsletter</div>
<div class="abs email-field">Email address</div>
<div class="abs subscribe">Subscribe</div>

<div class="abs copyright">Copyright 2013 CORVELL TARN &nbsp;I&nbsp; All Rights Reserved &nbsp;I&nbsp; Leader in Stainless Steel Products</div>

</body>
</html>
```